Business Card & Stationary Design Project

We are looking for some creative direction for business cards and our stationary.

We are a global logistics firm that has recently changed its name to Marrick Global Logistics and we have a new website due out tomorrow (www.marrick.com.au).

The colours of the company are rich navy tones, I would like to have business cards that fit together to make one picture on the back (possibly an old map of the world??), and the front to be modern contemporary looking.

But I am open to suggestions, so just incorporate our new logo and get going!
Updates

Hi Everyone,

Thank you for all of your designs so far and the time you have put into it.

I have asked many of you for amendments to see if we can get a final product, so with this in mind I am extending the deadline by a few days.

Good luck and thank you once again.

Please message me direct if you need any clarification.

Kind Regards
Colin

Reason: As outlined the extra 3 days is for amendments and changes to the current submissions. Thanks Colin

Industry/Entity Type

Business

```html
<!DOCTYPE html>
<html lang="en">
<head>
<meta charset="utf-8">
<title>Marrick Global Logistics – Business Card</title>
<link rel="stylesheet" href="https://fonts.googleapis.com/css2?family=Crimson+Text:wght@400;600&display=swap">
<style>
  :root {
    --page: #ffffff;
    --front-top: #050506;
    --front-mid: #2a2b2d;
    --front-bottom: #6e7073;
    --back-left: #0a1a3c;
    --back-right: #1d3f86;
    --accent-blue: #2f6fd1;
    --text-light: #ffffff;
    --text-soft: #e2e4e8;
    --text-muted: #c9ccd2;
  }
  * { margin: 0; padding: 0; box-sizing: border-box; }
  html, body {
    width: 1063px;
    height: 1200px;
    overflow: hidden;
    background: var(--page);
    font-family: "Crimson Text", Georgia, serif;
  }
  .canvas { position: relative; width: 1063px; height: 1200px; }

  .card {
    position: absolute;
    top: 80px;
    width: 386px;
    height: 236px;
    overflow: hidden;
    color: var(--text-light);
  }
  .card-front { left: 104px; }
  .card-back { left: 553px; }

  .card-art { position: absolute; inset: 0; width: 100%; height: 100%; }

  /* Front */
  .brand {
    position: absolute;
    left: 12px;
    top: 19px;
    display: flex;
    align-items: center;
    gap: 8px;
  }
  .brand-name {
    font-weight: 400;
    color: var(--text-light);
    line-height: 1;
  }
  .brand-name .word-main { display: block; font-size: 15px; letter-spacing: 3px; }
  .brand-name .word-sub { display: block; font-size: 6.5px; letter-spacing: 1.6px; margin-top: 2px; }
  .brand-dot {
    width: 36px;
    height: 36px;
    border-radius: 50%;
    background: var(--accent-blue);
    margin-left: 4px;
  }

  .person {
    position: absolute;
    left: 0;
    right: 0;
    top: 88px;
    text-align: center;
  }
  .person-name { font-size: 25px; font-weight: 400; line-height: 1.1; letter-spacing: 0.2px; }
  .person-title { font-size: 13px; color: var(--text-soft); line-height: 1.2; }

  .contact {
    position: absolute;
    left: 12px;
    top: 165px;
    display: grid;
    grid-template-columns: 44px auto;
    row-gap: 3px;
    font-size: 11.5px;
    line-height: 1.45;
  }
  .contact-label { color: var(--text-muted); }
  .contact-value { color: var(--text-light); font-weight: 600; }

  .address {
    position: absolute;
    right: 21px;
    top: 168px;
    text-align: right;
    font-size: 11.5px;
    font-style: normal;
    font-weight: 600;
    line-height: 1.42;
  }

  /* Back */
  .back-brand {
    position: absolute;
    left: 0;
    right: 0;
    top: 94px;
    text-align: center;
    font-weight: 400;
    color: var(--text-light);
    line-height: 1;
  }
  .back-brand .word-main { display: block; font-size: 36px; letter-spacing: 9px; padding-left: 9px; }
  .back-brand .word-sub { display: block; font-size: 13px; letter-spacing: 4.5px; margin-top: 1px; }
</style>
</head>
<body>
<main class="canvas">

  <section class="card card-front" aria-label="Business card front">
    <svg class="card-art" viewBox="0 0 386 236" role="img" aria-label="World map with globe grid lines in dark grey tones" preserveAspectRatio="none">
      <defs>
        <linearGradient id="frontShade" x1="0" y1="0" x2="0" y2="1">
          <stop offset="0" stop-color="var(--front-top)"/>
          <stop offset="0.5" stop-color="var(--front-mid)"/>
          <stop offset="1" stop-color="var(--front-bottom)"/>
        </linearGradient>
      </defs>
      <rect width="386" height="236" fill="url(#frontShade)"/>
    </svg>

    <div class="brand">
      <p class="brand-name">
        <span class="word-main">MARRICK</span>
        <span class="word-sub">GLOBAL LOGISTICS</span>
      </p>
      <span class="brand-dot" aria-hidden="true"></span>
    </div>

    <div class="person">
      <h1 class="person-name">Colin Ashdown</h1>
      <p class="person-title">General Manager</p>
    </div>

    <dl class="contact">
      <dt class="contact-label">mail.</dt><dd class="contact-value">colin@marrick.com.au</dd>
      <dt class="contact-label">tel.</dt><dd class="contact-value">+61 2 5550 1240</dd>
      <dt class="contact-label">web.</dt><dd class="contact-value">www.marrick.com.au</dd>
    </dl>

    <address class="address">
      58 Harbourview Ln,<br>
      Millbrook,<br>
      QLD, 4017, Australia
    </address>
  </section>

  <section class="card card-back" aria-label="Business card back">
    <svg class="card-art" viewBox="0 0 386 236" role="img" aria-label="World map with globe grid lines in navy and light blue tones" preserveAspectRatio="none">
      <defs>
        <linearGradient id="backShade" x1="0" y1="0" x2="1" y2="0">
          <stop offset="0" stop-color="var(--back-left)"/>
          <stop offset="1" stop-color="var(--back-right)"/>
        </linearGradient>
      </defs>
      <rect width="386" height="236" fill="url(#backShade)"/>
    </svg>

    <p class="back-brand">
      <span class="word-main">MARRICK</span>
      <span class="word-sub">GLOBAL LOGISTICS</span>
    </p>
  </section>

</main>
</body>
</html>
```